EVACUATION SIGNS FOR CABINS

ATTACHED ARE EVACUATION PLANS FOR OUR CABINS.
1. IS A BLANK EVACUTION SIGN & DIAGRAM FOR YOU TO ADD THE THREE DIFFERENT TYPES OF CABINS WE HAVE.
2. DESIGN, A EVACUTION SIGN & DIAGRAM FOR EACH CABIN STYLE.
WITH LEGEND ON EACH ONE SHOWING WHAT IS IN EACH CABIN FOR FIRE SAFETY.

```html
<!DOCTYPE html>
<html lang="en">
<head>
<meta charset="utf-8">
<title>Evacuation Sign &amp; Diagram – Chalets</title>
<link rel="stylesheet" href="https://fonts.googleapis.com/css2?family=Arimo:wght@400;700&family=Tinos:wght@400;700&display=swap">
<style>
:root{
  --frame-blue:#1b1bd6;
  --alarm-red:#e0141b;
  --safety-green:#1f9a3a;
  --lime:#9ad12b;
  --ink:#111;
  --stage-blue:#2231c8;
  --paper:#fff;
  --plan-grey:#e6e6e6;
  --box-line:#222;
}
*{box-sizing:border-box;margin:0;padding:0}
html,body{width:850px;height:1200px;overflow:hidden;background:var(--paper)}
body{position:relative;font-family:"Arimo",Arial,sans-serif;color:var(--ink)}
.sign-frame{position:absolute;left:26px;top:12px;width:808px;height:1164px;border:4px solid var(--frame-blue)}
.sign-title{position:absolute;left:0;width:850px;top:56px;text-align:center;color:var(--alarm-red);font-weight:700;font-size:25px;letter-spacing:.3px}
.site-name,.site-address{position:absolute;left:0;width:850px;text-align:center;font-weight:700;font-size:12.5px}
.site-name{top:88px}.site-address{top:104px}
.cabin-type{position:absolute;left:0;width:850px;top:176px;text-align:center;font-weight:700;font-size:19px}

.plan-legend{position:absolute;left:29px;top:256px;width:148px;height:167px;border:1.5px solid var(--box-line);font-family:"Tinos",serif;font-size:13px;padding:8px 6px}
.plan-legend h3{font-weight:400;font-size:13px;margin-bottom:10px}
.legend-row{display:flex;align-items:center;height:28px;gap:8px}
.legend-row span{width:66px}
.exit-chip{width:62px;height:22px;background:var(--safety-green);color:#fff;font:700 8px "Arimo",sans-serif;display:flex;align-items:center;justify-content:center}

.floor-plan{position:absolute;left:245px;top:242px;width:540px;height:328px;background:linear-gradient(180deg,#eeeeee,#d9d9d9)}

.icon-strip{position:absolute;left:34px;top:608px;width:780px;height:40px}
.icon-strip svg{position:absolute;top:0}

.panel{position:absolute;border:2px solid var(--box-line);background:var(--paper)}
.panel h2{color:var(--alarm-red);font-size:14px;font-weight:700;text-align:center;margin:6px 0 6px}
.evac-procedures{left:32px;top:658px;width:505px;height:157px;padding:0 8px}
.stage{font-size:9px;line-height:1.2}
.stage b{color:var(--stage-blue)}
.stage b em{font-style:normal;color:var(--alarm-red)}
.stage p{font-size:7.5px;margin-bottom:3px}
.stage p strong{color:var(--alarm-red)}
.stage .assembly{color:var(--safety-green)}

.safety-measures{left:547px;top:658px;width:271px;height:157px;padding:0 8px}
.safety-measures h2{color:var(--stage-blue)}
.safety-measures ul{font-size:9.5px;padding-left:12px;line-height:1.25}
.safety-measures strong{color:var(--alarm-red)}
.mobility{display:flex;gap:12px;margin-top:8px;align-items:center}
.mobility p{border:1.5px solid var(--box-line);font-family:"Tinos",serif;font-weight:700;font-size:10.5px;padding:3px 5px;width:160px;line-height:1.15}
.access-mark{width:70px;height:66px;border:1.5px solid var(--box-line);display:flex;align-items:center;justify-content:center}

.extinguisher-use{left:32px;top:824px;width:336px;height:148px;padding:0 10px}
.extinguisher-use ul{font-size:8.5px;padding-left:22px;line-height:1.35}
.extinguisher-use ul ul{list-style:square;padding-left:16px}
.extinguisher-use .last{font-size:8.5px;margin-top:2px}

.fire-equipment{left:32px;top:979px;width:336px;height:185px;padding:0 10px;text-align:center}
.fire-equipment .installed{font-size:9.5px;margin-top:6px}
.fire-equipment .type{font-size:14px;font-weight:700;margin:8px 0 10px}
.fire-equipment .check{font-size:8.5px;display:flex;justify-content:center;align-items:center;gap:6px}
.fire-equipment .warn{font-size:8.5px;text-align:left;margin-top:12px}

.symbol-key{left:377px;top:824px;width:186px;height:340px;padding:10px 8px}
.key-row{display:flex;align-items:center;gap:8px;height:25.5px}
.key-row .sym{width:32px;display:flex;justify-content:center}
.key-row .name{flex:1;border:1px solid var(--box-line);font-size:7.5px;padding:3px 4px;min-height:16px;display:flex;align-items:center}

.fire-steps{left:569px;top:824px;width:249px;height:340px;padding:20px 10px 0 10px;font-family:"Tinos",serif;color:var(--alarm-red)}
.fire-steps .headline{border:1.5px solid var(--box-line);padding:4px 8px;width:190px;margin-left:10px}
.fire-steps .headline h3{font-size:19px;font-weight:700;letter-spacing:-.3px}
.fire-steps .headline p{font-size:9px;}
.race-step{margin-top:14px}
.race-step h4{font-weight:400;font-size:18px}
.race-step h4 .cap{font-size:32px}
.race-step p{font-size:6.5px;color:var(--ink);padding-left:30px;text-transform:uppercase}
.race-step p span{color:var(--alarm-red)}
</style>
</head>
<body>
<div class="sign-frame"></div>

<h1 class="sign-title">EVACUATION SIGN &amp; DIAGRAM</h1>
<div class="site-name">CORAL BEND HOLIDAY PARK</div>
<div class="site-address">218 SHORELINE ROAD, TALLOW BAY, QLD. 4810</div>
<div class="cabin-type">CHALETS</div>

<div class="plan-legend">
  <h3>LEGEND</h3>
  <div class="legend-row"><span>Exit Sign -</span><div class="exit-chip">EXIT</div></div>
  <div class="legend-row"><span>Exit Path -</span><svg width="60" height="12"><line x1="2" y1="6" x2="48" y2="6" stroke="#e0141b" stroke-width="3"/><polygon points="46,1 58,6 46,11" fill="#e0141b"/></svg></div>
  <div class="legend-row"><span>Fire Blanket –</span><svg width="20" height="26"><rect x="3" y="2" width="14" height="22" rx="4" fill="#e0141b"/></svg></div>
  <div class="legend-row"><span>Fire Alarms -</span><svg width="24" height="16"><ellipse cx="12" cy="5" rx="9" ry="3" fill="#fff" stroke="#111"/><path d="M3 5v6a9 3 0 0 0 18 0V5" fill="#fff" stroke="#111"/></svg></div>
</div>

<div class="floor-plan" role="img" aria-label="Chalet floor plan with two bedrooms, kitchen, bathroom, lounge and deck, showing exit path arrow to the exit sign at the deck door"></div>

<div class="icon-strip">
  <svg style="left:0" width="54" height="36"><rect x="4" y="6" width="9" height="26" rx="3" fill="#e0141b"/><rect x="22" y="6" width="9" height="26" rx="3" fill="#e0141b"/><rect x="22" y="16" width="9" height="4" fill="#1b3fa0"/><rect x="40" y="6" width="9" height="26" rx="3" fill="#e0141b"/><rect x="40" y="16" width="9" height="4" fill="#fff"/></svg>
  <svg style="left:228px" width="46" height="26"><rect x="1" y="1" width="44" height="24" fill="#1f9a3a" stroke="#111"/><text x="23" y="17" text-anchor="middle" fill="#fff" font-size="9" font-weight="700" font-family="Arimo">AA</text></svg>
  <svg style="left:300px" width="30" height="26"><line x1="2" y1="13" x2="28" y2="13" stroke="#9ad12b" stroke-width="5"/></svg>
  <svg style="left:338px" width="40" height="26"><rect x="1" y="6" width="26" height="14" fill="#9ad12b" stroke="#111"/><polygon points="27,2 38,13 27,24" fill="#9ad12b" stroke="#111"/></svg>
  <svg style="left:385px" width="30" height="26"><rect x="1" y="1" width="28" height="24" fill="#e0141b"/><path d="M8 18l8-6v4l6-5" stroke="#fff" stroke-width="2.5" fill="none"/></svg>
  <svg style="left:422px" width="30" height="26"><rect x="1" y="1" width="28" height="24" fill="#1f9a3a"/><path d="M15 5v16M7 13h16" stroke="#fff" stroke-width="6"/></svg>
  <svg style="left:459px" width="34" height="26"><rect x="1" y="1" width="32" height="24" fill="#e0141b"/><text x="17" y="18" text-anchor="middle" fill="#fff" font-size="12" font-weight="700" font-family="Arimo">FB</text></svg>
  <svg style="left:500px" width="26" height="26"><circle cx="13" cy="13" r="11" fill="#e0141b"/><circle cx="13" cy="13" r="6" fill="#fff"/><circle cx="13" cy="13" r="3" fill="#e0141b"/></svg>
  <svg style="left:532px" width="38" height="26"><rect x="1" y="1" width="36" height="24" fill="#1f9a3a"/><text x="19" y="18" text-anchor="middle" fill="#fff" font-size="12" font-weight="700" font-family="Arimo">EXIT</text></svg>
  <svg style="left:576px" width="30" height="30"><rect x="1" y="1" width="28" height="28" fill="#e0141b"/><rect x="7" y="8" width="16" height="12" fill="#ffb400"/></svg>
  <svg style="left:614px" width="26" height="26"><rect x="1" y="3" width="24" height="20" fill="#e0141b"/><rect x="7" y="8" width="12" height="10" fill="#fff"/><circle cx="13" cy="13" r="2.5" fill="#e0141b"/></svg>
</div>

<section class="panel evac-procedures">
  <h2><u>EVACUATION PROCEDURES</u></h2>
  <div class="stage">
    <b>STAGE 1:- Removal <span style="font-weight:400">of people from the immediate Danger Area</span></b>
    <p>Occupants and staff in the immediate danger area are to assemble a safe distance away from the fire and smoke. When the area has been vacated all doors and windows should be closed to contain fire.</p>
    <b>STAGE 2:- Removal to a Safe Area</b>
    <p>If the severity of the smoke or fire warrants further <b style="color:inherit">evacuation</b>, occupants should be moved through fire / smoke doors to a safe area.</p>
    <b>STAGE 3:- Complete Evacuation of Entire Complex</b>
    <p>Should the emergency escalate, everyone is to leave every building by the nearest exit and move to the assembly area without delay.</p>
    <b>STAGE 4:- Roll Call.</b>
    <p>To be conducted as soon as possible and to ensure all Persons are accounted for. Report all missing persons to <strong>FIRE OFFICERS</strong>.</p>
    <b><em>STAGE 5:-</em> <span class="assembly">ASSEMBLY AREA</span></b>
  </div>
</section>

<section class="panel safety-measures">
  <h2><u>SAFETY MEASURES</u></h2>
  <ul>
    <li>Always turn off all electrical appliances and shut all doors.</li>
    <li>Your first role is life safety. Only attempt to extinguish fire <strong>IF SAFE TO DO SO.</strong></li>
  </ul>
  <div class="mobility">
    <p>Mobility impaired persons should evacuate immediately on hearing the fire alarm assisted by a nominated person.</p>
    <div class="access-mark"><svg width="58" height="56" viewBox="0 0 58 56"><rect width="58" height="56" fill="#111"/><circle cx="26" cy="10" r="5" fill="#fff"/><path d="M26 17v15h14l5 12" stroke="#fff" stroke-width="4" fill="none"/><path d="M20 26a12 12 0 1 0 14 18" stroke="#fff" stroke-width="3.5" fill="none"/></svg></div>
  </div>
</section>

<section class="panel extinguisher-use">
  <h2><u>FIRE EXTINGUISHER OPERATION</u></h2>
  <ul>
    <li>Stand well back from fire (3 M)</li>
    <li>Always face the fire with your back to a clear doorway</li>
    <li>Always be in pairs.</li>
    <li>Use the PASS method
      <ul>
        <li>P - pull the pin</li>
        <li>A - aim at edge of fire</li>
        <li>S - squeeze the handle</li>
        <li>S - sweep the fire</li>
      </ul>
    </li>
  </ul>
  <p class="last">As the fire diminishes, slowly move closer towards the FIRE staying 1 m</p>
</section>

<section class="panel fire-equipment">
  <h2><u>FIRE FIGHTING EQUIPMENT</u></h2>
  <p class="installed">Installed in this building are:</p>
  <p class="type">Dry Powder Extinguishers (red with white band)</p>
  <p class="check">Check the Extinguisher label for instructions. <svg width="16" height="24"><rect x="3" y="3" width="10" height="20" rx="3" fill="#e0141b"/><rect x="3" y="10" width="10" height="3" fill="#fff"/></svg></p>
  <p class="warn">Under no circumstances should you use water on or near live electrical equipment.</p>
</section>

<section class="panel symbol-key">
  <div class="key-row"><div class="sym"><svg width="24" height="24"><rect x="1" y="1" width="22" height="22" fill="#e0141b"/><circle cx="12" cy="12" r="7" fill="#fff"/><circle cx="12" cy="12" r="3" fill="#e0141b"/></svg></div><div class="name">HOSEREEL</div></div>
  <div class="key-row"><div class="sym"><svg width="24" height="24"><rect x="1" y="1" width="22" height="22" fill="#e0141b"/><rect x="6" y="7" width="12" height="9" fill="#ffb400"/></svg></div><div class="name">FIRE INDICATOR PANEL</div></div>
  <div class="key-row"><div class="sym"><svg width="24" height="24"><rect x="1" y="1" width="22" height="22" fill="#e0141b"/><rect x="6" y="6" width="12" height="12" fill="#fff"/><circle cx="12" cy="12" r="3" fill="#e0141b"/></svg></div><div class="name">MANUAL CALL POINT</div></div>
  <div class="key-row"><div class="sym"><svg width="14" height="24"><rect x="2" y="2" width="10" height="20" rx="3" fill="#e0141b"/><rect x="2" y="9" width="10" height="3" fill="#fff"/></svg></div><div class="name">EXTINGUISHER</div></div>
  <div class="key-row"><div class="sym"><svg width="28" height="20"><rect width="28" height="20" fill="#e0141b"/><text x="14" y="15" text-anchor="middle" fill="#fff" font-size="11" font-weight="700" font-family="Arimo">FB</text></svg></div><div class="name">FIRE BLANKET</div></div>
  <div class="key-row"><div class="sym"><svg width="26" height="20"><rect width="26" height="20" fill="#1f9a3a"/><path d="M13 3v14M6 10h14" stroke="#fff" stroke-width="5"/></svg></div><div class="name">FIRST AID</div></div>
  <div class="key-row"><div class="sym"><svg width="26" height="20"><rect width="26" height="20" fill="#e0141b"/><path d="M7 15l7-5v3l5-4" stroke="#fff" stroke-width="2" fill="none"/></svg></div><div class="name">SWITCH BOARD</div></div>
  <div class="key-row"><div class="sym"><svg width="30" height="18"><rect width="30" height="18" fill="#1f9a3a"/><text x="15" y="13" text-anchor="middle" fill="#fff" font-size="9" font-weight="700" font-family="Arimo">EXIT</text></svg></div><div class="name">EXIT SIGN</div></div>
  <div class="key-row"><div class="sym"><svg width="32" height="18"><rect x="1" y="5" width="20" height="8" fill="#9ad12b" stroke="#111"/><polygon points="21,1 31,9 21,17" fill="#9ad12b" stroke="#111"/></svg></div><div class="name">PATH OF EXIT</div></div>
  <div class="key-row"><div class="sym"><svg width="30" height="10"><line x1="0" y1="5" x2="30" y2="5" stroke="#9ad12b" stroke-width="5"/></svg></div><div class="name">MAIN PATH</div></div>
  <div class="key-row"><div class="sym"><svg width="30" height="10"><line x1="0" y1="5" x2="30" y2="5" stroke="#9ad12b" stroke-width="5" stroke-dasharray="5 3"/></svg></div><div class="name">ALTERNATE PATH</div></div>
  <div class="key-row"><div class="sym"><svg width="28" height="18"><rect width="28" height="18" fill="#1f9a3a"/><text x="14" y="13" text-anchor="middle" fill="#fff" font-size="8" font-weight="700" font-family="Arimo">AA</text></svg></div><div class="name">ASSEMBLY AREA</div></div>
</section>

<section class="panel fire-steps">
  <div class="headline">
    <h3>IN CASE OF FIRE</h3>
    <p>FIRE / EVACUATION PROCEDURES</p>
  </div>
  <div class="race-step"><h4><span class="cap">R</span>EMOVE PEOPLE</h4><p>If in danger to the <span>assembly point</span></p></div>
  <div class="race-step"><h4><span class="cap">A</span>LERT THE FIRE SERVICE</h4><p>Nearby residents and members of the public</p></div>
  <div class="race-step"><h4><span class="cap">C</span>ONFINE FIRE &amp; SMOKE</h4><p>Close all windows &amp; doors (if safe to do so)</p></div>
  <div class="race-step"><h4><span class="cap">E</span>XTINGUISH</h4><p>And control the fire (if safe to do so)</p></div>
</section>
</body>
</html>
```